Business card design needed

We need something on the back that allows the customer to get five stamps then the sixth visit they get 25 dollars to spend.
Industry/Entity Type
Business
Contact Information for Business Card
Quality meat,value for money,spit roast hire, wholesale pubs clubs,cater for bbqs.marlow lane butchery 217 marlow lane.64739204.

```html
<!DOCTYPE html>
<html lang="en">
<head>
<meta charset="utf-8">
<title>Marlow Lane Butchery – Business and Loyalty Cards</title>
<link rel="stylesheet" href="https://fonts.googleapis.com/css2?family=Limelight&family=Josefin+Sans:ital,wght@0,300;0,400;1,300&display=swap">
<style>
  :root {
    --navy: #0e3470;
    --navy-deep: #0a2a5c;
    --sky: #7fb0d6;
    --paper: #f4f5f4;
    --ink: #17306a;
    --stage: #e6e6e4;
    --illus-a: #6a9cc4;
    --illus-b: #1d4a86;
  }
  * { box-sizing: border-box; margin: 0; padding: 0; }
  html, body { width: 1200px; height: 1200px; overflow: hidden; }
  body {
    background: var(--stage);
    font-family: "Josefin Sans", sans-serif;
    position: relative;
  }
  .card {
    position: absolute;
    left: 150px;
    width: 900px;
    height: 514px;
    overflow: hidden;
    box-shadow: 0 6px 18px rgba(0,0,0,.18);
  }

  /* Front */
  .card-front { top: 60px; background: var(--paper); }
  .front-band {
    position: absolute; left: 0; top: 0; width: 100%; height: 150px;
    background: var(--navy);
  }
  .front-band-side {
    position: absolute; right: 0; top: 150px; width: 330px; height: 130px;
    background: var(--navy);
  }
  .brand-name {
    position: absolute; left: 90px; top: 22px; width: 520px;
    font-family: "Limelight", serif;
    color: var(--sky);
    font-size: 54px; line-height: 54px; letter-spacing: 2px;
    text-align: center; text-transform: uppercase;
  }
  .tagline {
    position: absolute; left: 180px; top: 172px; width: 370px;
    color: var(--ink); font-style: italic; font-weight: 300;
    font-size: 15px; line-height: 21px; text-align: right;
    white-space: nowrap;
  }
  .butcher-illustration {
    position: absolute; left: 570px; top: 110px; width: 300px; height: 300px;
    background: linear-gradient(160deg, var(--illus-a), var(--illus-b));
    border: 3px solid var(--navy-deep);
  }
  .contact {
    position: absolute; left: 95px; top: 282px;
    color: var(--ink); font-weight: 300; font-size: 30px; line-height: 44px;
  }
  .contact .email { margin-top: 30px; }

  /* Back */
  .card-back { top: 626px; background: var(--navy); }
  .stripe {
    position: absolute; left: 0; width: 100%; height: 9px; background: var(--paper);
  }
  .back-title {
    position: absolute; left: 0; top: 26px; width: 100%;
    font-family: "Limelight", serif; color: var(--sky);
    font-size: 44px; text-align: center; text-transform: uppercase; letter-spacing: 2px;
  }
  .stamp-grid {
    position: absolute; left: 190px; top: 108px;
    display: grid; grid-template-columns: repeat(3, 150px); gap: 24px 30px;
  }
  .stamp {
    width: 150px; height: 138px; background: var(--paper);
    border: 3px solid var(--sky);
    display: flex; align-items: center; justify-content: center;
    font-family: "Limelight", serif; color: var(--sky); font-size: 42px;
    text-align: center; line-height: 44px;
  }
  .stamp-reward { font-size: 36px; }
  .back-note {
    position: absolute; left: 0; bottom: 0; width: 100%; height: 58px;
    background: var(--navy-deep);
    color: var(--sky); font-style: italic; font-weight: 300; font-size: 24px;
    display: flex; align-items: center; justify-content: center;
  }
</style>
</head>
<body>
  <section class="card card-front">
    <div class="front-band"></div>
    <div class="front-band-side"></div>
    <h1 class="brand-name">Marlow Lane<br>Butchery</h1>
    <p class="tagline">Quality Meat, Value for Money, Spit Roast Hire,<br>Wholesale Pubs/Clubs, Cater for BBQs.</p>
    <div class="butcher-illustration" role="img" aria-label="Illustration of a butcher in a white coat and cap carving a cut of meat on a board"></div>
    <div class="contact">
      <p>217 Marlow Lane</p>
      <p>p: 02 64739204</p>
      <p class="email">e: marlowlnbutchery@tinmail.com</p>
    </div>
  </section>

  <section class="card card-back">
    <div class="stripe" style="top:14px"></div>
    <div class="stripe" style="top:150px"></div>
    <div class="stripe" style="top:262px"></div>
    <div class="stripe" style="top:374px"></div>
    <h2 class="back-title">Marlow Lane Butchery</h2>
    <div class="stamp-grid">
      <div class="stamp">1</div>
      <div class="stamp">2</div>
      <div class="stamp">3</div>
      <div class="stamp">4</div>
      <div class="stamp">5</div>
      <div class="stamp stamp-reward">$25<br>OFF</div>
    </div>
    <p class="back-note">Spend $50 or more to recieve a stamp. Recieve $25 off your 6th visit!</p>
  </section>
</body>
</html>
```